Education Foundation Needs a Flyer for an Awareness/Fundraising Event

We need a flyer design for our Education Celebration that is held each year to commemorate Lone Prairie Learning Week.

This event provides an excellent opportunity for the community to come together to celebrate the education of our children and support the Brisbane Ridge Unified School District. All twelve schools in the district will have tabletop displays highlighting some of their activities during the year. Teachers will also have grant displays to spotlight the innovative classroom projects they implemented due to funding provided by the Brisbane Ridge Education Foundation.

The evening will also include entertainment provided by BRUSD school choirs. The event concludes with drawing for prices, and a raffle drawing.

Listed below are the details that need to be included in the flyer. I have also included our logo that must be used. I also included some photos from past celebrations that may or may not be helpful.

Please join the Brisbane Ridge Education Foundation as we celebrate BRUSD and its students, educational programs, and schools.

Thursday, March 26, 2015
5:00 p.m. – 8:00 p.m.
Brisbane Ridge High School

Students: Please sign up to be entered in a drawing for Kumora Pocket.
Adults: Please sign up to be entered in a drawing for a $50 Shopwell Gift Card.

Raffle Prizes
TELVANA 50" Class 1080p LED Smart HDTV
Zentra Play Console w/ Motionpad
Donations of $2 each or 3 for $5, or 7 for $10
*Tickets are available at the BRUSD Administration Building/ Communications and at the schools. (You must be present to win.)

Prizes Galore!
• Campus with the highest percentage of adult attendance will win $300 + the Traveling
Trophy for one year.
• Campus with the 2nd highest percentage of adult attendance will win $150.
• Additional drawings for Teacher, Principal/ Asst. Principal, and District Personnel will be held.

Your Choice – Your Prize
Drawings

7" Orvel NEBULA Pad 4
Brightline Streamstick
Brewmont Classic B30 Single Serve
External Hard Drive
Brewmont 3.0 B700 Coffee Brewing System w/ Carafe
Brightline Streamstick
Cotton Candy Maker
*For your donation of $1.00 per ticket, you may place your ticket(s) in one or all of the baskets. It’s your choice. (You must be present to win.)

Food!
Hot Dogs $1.00
Corn Dogs $0.75
Chips $0.50
Drinks $0.75
Cookies $0.75
Baskets - $2.50 (Hot Dog or Corn Dog, Chips, Drink, Cookie)

For more information, please call 555-318-2946.

```html
<!DOCTYPE html>
<html lang="en">
<head>
<meta charset="utf-8">
<title>Brisbane Ridge Education Foundation – Education Celebration Flyer</title>
<link rel="stylesheet" href="https://fonts.googleapis.com/css2?family=Oswald:wght@500;600;700&family=Open+Sans:wght@400;600;700&display=swap">
<style>
  :root{
    --bg:#e4e4e2;
    --paper:#ffffff;
    --navy:#1f3f8f;
    --blue:#2d56b0;
    --band-light:#4a72c4;
    --gold:#f2c230;
    --red:#b3262c;
    --ink:#2c2c2c;
    --grey:#bdbdbd;
    --photo-a:#c9a27a;
    --photo-b:#6b7fa8;
  }
  *{margin:0;padding:0;box-sizing:border-box}
  html,body{width:1200px;height:928px;overflow:hidden;background:var(--bg)}
  body{display:flex;align-items:center;justify-content:center;font-family:"Open Sans",Arial,sans-serif;color:var(--ink)}
  .flyer{width:680px;height:880px;background:var(--paper);position:relative;box-shadow:0 6px 18px rgba(0,0,0,.25);overflow:hidden}
  .hero-photo{height:290px;background:linear-gradient(160deg,var(--photo-a) 0%,#b98f6d 40%,var(--photo-b) 100%)}
  .title-band{min-height:100px;background:linear-gradient(100deg,var(--navy) 0%,var(--blue) 45%,var(--band-light) 100%);text-align:center;padding:14px 10px 12px;color:#fff}
  .title-band h1{font-family:"Oswald",Arial,sans-serif;font-weight:700;color:var(--gold);font-size:26px;letter-spacing:.8px;line-height:1.15;white-space:nowrap}
  .title-band .tagline{font-size:13px;margin-top:4px;white-space:nowrap}
  .title-band .when{font-family:"Oswald",Arial,sans-serif;font-weight:500;font-size:13.5px;color:var(--gold);margin-top:4px;letter-spacing:.4px;white-space:nowrap}
  .body{display:flex;gap:26px;padding:16px 30px 0 34px}
  .col-left{width:290px;font-size:11.5px;line-height:1.4}
  .col-right{flex:1;font-size:11.5px;line-height:1.4}
  .section-head{font-family:"Oswald",Arial,sans-serif;font-weight:600;color:var(--blue);font-size:17px;margin:4px 0 2px}
  .choice-head{font-family:"Oswald",Arial,sans-serif;font-weight:700;color:var(--red);font-size:24px;line-height:1.15;margin-bottom:2px;white-space:nowrap}
  .note{font-size:10.5px}
  ul.bullets{list-style:none;margin-top:2px}
  ul.bullets li{padding-left:12px;position:relative;margin-bottom:3px}
  ul.bullets li::before{content:"•";position:absolute;left:0}
  .signup{margin-top:14px;font-size:10.5px}
  .signup b{color:var(--red);display:block}
  .footer{position:absolute;left:0;right:0;bottom:0;height:82px}
  .footer-grey{position:absolute;left:0;bottom:0;width:260px;height:82px;background:var(--grey);display:flex;flex-direction:column;align-items:center;justify-content:center;gap:4px}
  .logo{display:flex;align-items:center;gap:6px;font-family:"Oswald",Arial,sans-serif;font-weight:600;color:var(--navy);font-size:16px}
  .logo .dot{width:18px;height:18px;border-radius:50%;background:var(--navy)}
  .web{font-size:9.5px;color:#444}
  .footer-blue{position:absolute;right:0;bottom:0;width:440px;height:82px;background:var(--navy);clip-path:polygon(0 38%,100% 0,100% 100%,0 100%);display:flex;align-items:flex-end;justify-content:center;padding-bottom:18px;gap:8px;color:#fff;font-family:"Oswald",Arial,sans-serif;font-weight:500;font-size:16px}
  .footer-blue .phone{color:var(--gold);font-size:22px;font-weight:700;line-height:1}
</style>
</head>
<body>
<main class="flyer">
  <div class="hero-photo" role="img" aria-label="Photo of smiling students and teachers gathered at a past education celebration"></div>

  <header class="title-band">
    <h1>JOIN THE BRISBANE RIDGE EDUCATION FOUNDATION</h1>
    <p class="tagline">as we celebrate BRUSD and its students, educational programs, and schools</p>
    <p class="when">Thursday, March 26, 2015 &nbsp;|&nbsp; 5:00 p.m. – 8:00 p.m. &nbsp;|&nbsp; Brisbane Ridge High School</p>
  </header>

  <section class="body">
    <div class="col-left">
      <h2 class="section-head">Raffle Prizes</h2>
      <p>TELVANA 50" Class 1080p LED Smart HDTV<br>Zentra Play Console w/ Motionpad<br>Donations of $2 each or 3 for $5, or 7 for $10</p>
      <p class="note">*Tickets are available at the BRUSD Administration Building/ Communications and at the schools. (You must be present to win.)</p>

      <h2 class="section-head">Prizes Galore!</h2>
      <ul class="bullets">
        <li>Campus with the highest percentage of adult attendance will win $300 + the Traveling Trophy for one year.</li>
        <li>Campus with the 2nd highest percentage of adult attendance will win $150.</li>
        <li>Additional drawings for Teacher, Principal/ Asst. Principal, and District Personnel will be held.</li>
      </ul>

      <div class="signup">
        <p><b>Students:</b>Please sign up to be entered in a drawing for Kumora Pocket.</p>
        <p><b>Adults:</b>Please sign up to be entered in a drawing for a $50 Shopwell Gift Card.</p>
      </div>
    </div>

    <div class="col-right">
      <h2 class="choice-head">YOUR CHOICE - YOUR PRIZE</h2>
      <h3 class="section-head">Drawings</h3>
      <p>7" Orvel NEBULA Pad 4<br>Brightline Streamstick<br>Brewmont Classic B30 Single Serve<br>External Hard Drive<br>Brewmont 3.0 B700 Coffee Brewing System w/ Carafe<br>Brightline Streamstick<br>Cotton Candy Maker</p>
      <p class="note">*For your donation of $1.00 per ticket, you may place your ticket(s) in one or all of the baskets. It’s your choice. (You must be present to win.)</p>

      <h3 class="section-head">Food!</h3>
      <p>Hot Dogs $1.00<br>Corn Dogs $0.75<br>Chips $0.50<br>Drinks $0.75<br>Cookies $0.75<br>Baskets - $2.50 (Hot Dog or Corn Dog, Chips, Drink, Cookie)</p>
    </div>
  </section>

  <footer class="footer">
    <div class="footer-grey">
      <div class="logo"><span class="dot"></span>BREF</div>
      <p class="web">www.brisbaneridgefoundation.org</p>
    </div>
    <div class="footer-blue">
      <span>For more information please call:</span>
      <span class="phone">555-318-2946</span>
    </div>
  </footer>
</main>
</body>
</html>
```